Qamra
قمرة كافيه
Hello Designers:-
Please check your e-mail inbox.
Thank you so much!
plz star rating...
The front and the back of the card should be one color "Beige". In front, it only shows the logo, the address, e-mail, twitter and instagram accounts. No need to type any other word like the word "قمرة"
As for the back, we want a loyalty card with 6 stamps with "Qamra" shape drawing on each. and the 6th qamra has a FREE written on it (Pic provided in brief)
If you have any comments, questions or requirements please do not hesitate to contact me on my e-mail or here, in the discussion.
Thank you so much for your work! :)
Hello designers: Please make sure to read the project brief as we want a (Double) sided business card/loyalty card. Moreover, please be aware that the card color should follow the color of the store "Beige" and not the logo color (Store pic provided in the brief)
Thank you so much for your effort! And good luck!

```html
<!DOCTYPE html>
<html lang="en">
<head>
<meta charset="utf-8">
<title>Qamra – Business &amp; Loyalty Card</title>
<link href="https://fonts.googleapis.com/css2?family=Cairo:wght@300;400&family=Oswald:wght@500&family=Open+Sans:wght@400&display=swap" rel="stylesheet">
<style>
  :root {
    --backdrop: #e6e2dc;
    --beige: #c6a57c;
    --ink: #ffffff;
    --stamp-line: #ffffff;
    --art-tone: rgba(255,255,255,0.35);
    --art-tone-soft: rgba(255,255,255,0.18);
  }
  * { margin: 0; padding: 0; box-sizing: border-box; }
  html, body { width: 1200px; height: 389px; overflow: hidden; background: var(--backdrop); }
  .canvas { position: relative; width: 1200px; height: 389px; }

  .card {
    position: absolute; top: 24px; height: 353px; background: var(--beige);
    box-shadow: 0 2px 6px rgba(0,0,0,0.18); color: var(--ink);
  }
  .card--front { left: 5px; width: 578px; }
  .card--back  { left: 600px; width: 593px; }

  /* Front */
  .brand-mark {
    position: absolute; left: 210px; top: 50px; width: 170px; height: 140px;
    display: flex; align-items: center; justify-content: center;
    font-family: "Cairo", sans-serif; font-weight: 300; font-size: 76px; line-height: 1;
    color: var(--ink);
  }
  .contact { position: absolute; left: 238px; top: 216px; list-style: none; }
  .contact__item {
    display: flex; align-items: center; gap: 8px; height: 24px;
    font-family: "Open Sans", sans-serif; font-size: 12px; color: var(--ink);
    white-space: nowrap;
  }
  .contact__item--address { font-family: "Cairo", sans-serif; font-size: 12px; direction: rtl; justify-content: flex-end; }
  .contact__icon { width: 15px; height: 15px; flex: none; }

  /* Back */
  .stamp { position: absolute; width: 84px; }
  .stamp__label {
    display: block; text-align: center; font-family: "Oswald", sans-serif; font-weight: 500;
    font-size: 24px; line-height: 30px; color: var(--ink);
  }
  .stamp__box {
    width: 84px; height: 72px; border: 3px solid var(--stamp-line); border-radius: 12px;
    display: flex; align-items: center; justify-content: center;
  }
  .stamp__art {
    width: 40px; height: 54px; border-radius: 6px;
    background: linear-gradient(180deg, var(--art-tone), var(--art-tone-soft));
  }
  .stamp--1 { left: 45px;  top: 21px; }
  .stamp--2 { left: 170px; top: 21px; }
  .stamp--3 { left: 295px; top: 21px; }
  .stamp--4 { left: 45px;  top: 136px; }
  .stamp--free { left: 170px; top: 160px; }
  .stamp--5 { left: 295px; top: 136px; }

  .offer {
    position: absolute; left: 43px; top: 278px;
    font-family: "Oswald", sans-serif; font-weight: 500; font-size: 22px;
    letter-spacing: 1.6px; color: var(--ink); white-space: nowrap;
  }
  .flourish {
    position: absolute; left: 450px; top: 10px; width: 140px; height: 330px;
    background: radial-gradient(ellipse at 70% 50%, var(--art-tone-soft), transparent 70%);
  }
</style>
</head>
<body>
<main class="canvas">
  <section class="card card--front" aria-label="Business card front">
    <div class="brand-mark" lang="ar">قمرة</div>
    <ul class="contact">
      <li class="contact__item contact__item--address" lang="ar">جمعية واحة النخيل التعاونية - الطابق الأول</li>
      <li class="contact__item">
        <svg class="contact__icon" viewBox="0 0 16 16"><path d="M4 1h3l1 4-2 1a8 8 0 0 0 4 4l1-2 4 1v3c0 1-1 2-2 2A13 13 0 0 1 2 3c0-1 1-2 2-2z" fill="#fff"/></svg>
        55512340
      </li>
      <li class="contact__item">
        <svg class="contact__icon" viewBox="0 0 16 16"><rect x="1" y="3" width="14" height="10" rx="1" fill="none" stroke="#fff" stroke-width="1.5"/><path d="M1.5 3.5 8 9l6.5-5.5" fill="none" stroke="#fff" stroke-width="1.5"/></svg>
        QamraKuwait@example.com
      </li>
      <li class="contact__item">
        <svg class="contact__icon" viewBox="0 0 16 16"><circle cx="8" cy="8" r="7" fill="#fff"/></svg>
        @Qamra
      </li>
      <li class="contact__item">
        <svg class="contact__icon" viewBox="0 0 16 16"><rect x="1" y="1" width="14" height="14" rx="3" fill="#fff"/></svg>
        @QamraKuwait
      </li>
    </ul>
  </section>

  <section class="card card--back" aria-label="Loyalty card back">
    <div class="stamp stamp--1"><span class="stamp__label">1</span><div class="stamp__box"><div class="stamp__art" role="img" aria-label="Coffee pot drawing"></div></div></div>
    <div class="stamp stamp--2"><span class="stamp__label">2</span><div class="stamp__box"><div class="stamp__art" role="img" aria-label="Coffee pot drawing"></div></div></div>
    <div class="stamp stamp--3"><span class="stamp__label">3</span><div class="stamp__box"><div class="stamp__art" role="img" aria-label="Coffee pot drawing"></div></div></div>
    <div class="stamp stamp--4"><span class="stamp__label">4</span><div class="stamp__box"><div class="stamp__art" role="img" aria-label="Coffee pot drawing"></div></div></div>
    <div class="stamp stamp--free"><span class="stamp__label">FREE</span><div class="stamp__box"><div class="stamp__art" role="img" aria-label="Coffee pot drawing"></div></div></div>
    <div class="stamp stamp--5"><span class="stamp__label">5</span><div class="stamp__box"><div class="stamp__art" role="img" aria-label="Coffee pot drawing"></div></div></div>
    <p class="offer">Buy 5 AND GET ONE COFFEE REFILL FREE</p>
    <div class="flourish" role="img" aria-label="Decorative white floral swirl"></div>
  </section>
</main>
</body>
</html>
```